Candle Rental Business seeks new website design

We need a new website design for a Candle hire business. The business rents out pillar candles for events such as weddings and corporate events. Our main target market is weddings. The business name is Hire a Lantern. The business name does not have a logo design.

We would like a website that is light in colours and creates a warm atmosphere. The design needs to be elegant and upmarket. There are different size candles that we hire out, ranging from 10cm diameter to 20cm diameter, flat, tall etc. All our candles are white in colour. Its just the size that differs.

We would also like to include a section for hiring out decor such as glassvases, candlebras, overlays and chairs sachets, chair covers. However, this is not the businesses main focus but an additional offering to customers.

Target Market(s)

Wedding venues and brides. Corporate events. School dances.

Industry/Entity Type

Hospitality

Logo Text

Hire a Lantern

Number of Pages Required

1 page

Font styles to use
Sans Serif
Script

Requirements
Must have
• Pictures of pillar candles. Plain white candles. The website must centre around candles.
Nice to have
• Different examples of candle centrepieces
Should not have
• Pictures must not be of brides. Pictures of surrounding is perferable.

```html
<!DOCTYPE html>
<html lang="en">
<head>
<meta charset="utf-8">
<title>Hire a Lantern</title>
<link rel="stylesheet" href="https://fonts.googleapis.com/css2?family=Open+Sans:wght@400;600;700&family=Raleway:wght@500;600&display=swap">
<style>
:root{
  --red:#e31b23;
  --nav-red:#f0163d;
  --ink:#222;
  --muted:#777;
  --dark:#2f2f2f;
  --black:#000;
  --page:#fafafa;
  --band:#f0f0f0;
  --white:#fff;
  --social-a:#1877d2;
  --social-b:#10a7e8;
  --social-c:#1e4f6b;
}
*{box-sizing:border-box;margin:0;padding:0}
html,body{width:667px;height:1200px;overflow:hidden}
body{position:relative;background:var(--page);font-family:"Open Sans",sans-serif;color:var(--ink)}
.abs{position:absolute}
ul{list-style:none}

/* top bar */
.social-dots{left:26px;top:7px;display:flex;gap:15px}
.social-dots span{width:8px;height:8px;border-radius:50%;background:#555}
.social-dots span:first-child{background:var(--red)}
.account-links{left:488px;top:5px;font-size:6.4px;color:var(--muted);letter-spacing:.2px}
.account-links .login{color:var(--red)}
.search{left:26px;top:38px;width:201px;height:19px;display:flex}
.search input{flex:1;border:1px solid #ccc;border-right:0;font:5.6px "Open Sans",sans-serif;padding-left:8px;color:#999;background:var(--white)}
.search button{width:42px;background:var(--red);border:0;color:var(--white);font:600 6px "Open Sans",sans-serif}
.brand-name{font:600 13px "Raleway",sans-serif;color:var(--ink);white-space:nowrap;text-align:center}
.header-brand{left:283px;top:30px;width:140px}
.cart{left:547px;top:32px;width:95px;height:24px;border:1px solid #ddd;background:var(--white);display:flex;align-items:center;gap:5px;padding-left:7px;font-size:5.6px;color:var(--muted)}
.cart .caret{margin-left:auto;margin-right:6px;width:0;height:0;border-left:3px solid transparent;border-right:3px solid transparent;border-top:3px solid var(--red)}

/* navigation */
.nav{left:0;top:77px;width:667px;height:29px;background:var(--nav-red)}
.nav a{position:absolute;top:0;height:29px;line-height:29px;color:var(--white);font-size:5.8px;font-weight:600;text-decoration:none;transform:translateX(-50%);white-space:nowrap}
.nav .sep{position:absolute;top:0;width:1px;height:29px;background:rgba(255,255,255,.25)}
.nav .checkout{left:584px;width:58px;transform:none;background:var(--black);color:var(--white);text-align:center}

/* hero */
.hero{left:0;top:106px;width:667px;height:373px;background:var(--black);overflow:hidden}
.hero-photo{left:0;top:0;width:667px;height:373px;background:radial-gradient(ellipse 300px 260px at 170px 200px,#d08420 0%,#8a4a0e 35%,#2a1204 70%,#000 100%)}
.hero-copy{right:29px;top:137px;text-align:right;font-family:"Raleway",sans-serif;font-weight:500;color:var(--white);font-size:24.5px;line-height:30px;letter-spacing:.3px}
.hero-copy .hot{color:var(--red);font-weight:600}
.btn-solid{background:var(--red);color:var(--white);font-size:6.4px;font-weight:600;text-align:center}
.hero .shop{left:566px;top:242px;width:75px;height:19px;line-height:19px}
.dots{left:587px;top:289px;display:flex;gap:6px}
.dots span{width:8px;height:8px;border-radius:50%;border:1px solid var(--white)}
.dots span:first-child{background:var(--red);border-color:var(--red)}

/* category tiles */
.tile{overflow:hidden}
.tile-title{font-family:"Raleway",sans-serif;font-weight:500;text-align:center}
.btn-outline{border:1px solid var(--white);color:var(--white);font-size:6.2px;text-align:center}
.wedding{left:27px;top:490px;width:190px;height:138px;background:linear-gradient(160deg,#6b4a2e,#b88a5c 45%,#d9b88f 70%,#4a3020)}
.overlay-band{left:0;width:100%;height:42px;background:rgba(240,240,240,.72);color:var(--red);font-size:12px;line-height:42px}
.pillar{left:234px;top:490px;width:200px;height:286px;background:radial-gradient(ellipse at 50% 85%,#b2141e 0%,#5a0d12 35%,#1a0b0b 70%,#0b0b0b)}
.pillar .tile-title{top:20px;width:100%;color:var(--white);font-size:18px}
.pillar .btn-outline{left:64px;top:54px;width:54px;height:17px;line-height:15px}
.framed{border:1px solid #333;background:var(--white)}
.special{left:451px;top:490px;width:190px;height:138px}
.special .inner{left:4px;top:4px;width:180px;height:128px;background:var(--dark)}
.special .tile-title{top:42px;width:100%;color:var(--red);font-size:14px}
.special .btn-outline{left:65px;top:75px;width:53px;height:17px;line-height:15px}
.latest{left:27px;top:638px;width:190px;height:138px}
.latest .inner{left:6px;top:5px;width:177px;height:126px;background:var(--red)}
.latest .tile-title{top:28px;width:100%;color:var(--white);font-size:15px;line-height:19px}
.latest .btn-outline{left:48px;top:79px;width:54px;height:17px;line-height:15px}
.newmodel{left:454px;top:638px;width:189px;height:139px;background:linear-gradient(170deg,#3d2a1a,#a88b6b 40%,#e6d5bd 58%,#2c1c10)}

/* newsletter */
.newsletter{left:0;top:800px;width:667px;height:190px;background:var(--band)}
.section-title{font-family:"Raleway",sans-serif;font-weight:500;color:var(--red)}
.newsletter h2{left:30px;top:26px;font-size:17px}
.newsletter p{left:30px;top:58px;width:428px;font-size:6.1px;line-height:12.5px;color:#444}
.subscribe{left:30px;top:114px;width:415px;height:41px;display:flex}
.subscribe input{flex:1;border:1px solid #ddd;background:#f5f5f5;font:7.2px "Open Sans",sans-serif;padding-left:14px;color:#aaa}
.subscribe button{width:102px;border:0;background:var(--dark);color:var(--white);font:700 13px "Open Sans",sans-serif;letter-spacing:.5px}
.divider-v{left:478px;top:26px;width:1px;height:140px;background:#ccc}
.follow h2{left:478px;width:160px;top:22px;text-align:center;font-size:16px}
.follow a{position:absolute;left:501px;width:118px;height:28px;display:flex;align-items:center;gap:14px;padding-left:12px;color:var(--white);font-size:10.5px;font-weight:600;text-decoration:none;border-radius:2px}
.follow a::before{content:"";width:6px;height:6px;border-radius:50%;background:var(--white)}
.follow .a{top:55px;background:var(--social-a)}
.follow .b{top:91px;background:var(--social-b)}
.follow .c{top:129px;background:var(--social-c)}

/* footer */
.footer{left:0;top:990px;width:667px;height:156px;background:var(--page)}
.footer-brand{left:34px;top:82px;width:140px}
.footer .divider-v{top:22px;height:114px;background:#ddd}
.col{top:32px}
.col h3{font:600 8.8px "Raleway",sans-serif;color:var(--red);margin-bottom:7px}
.col li{font-size:5.8px;color:#888;line-height:16px;padding-left:6px;position:relative}
.col li::before{content:"";position:absolute;left:0;top:7px;width:2px;height:2px;border-radius:50%;background:#aaa}

/* bottom bar */
.legal{left:0;top:1146px;width:667px;height:54px;background:var(--red);color:var(--white)}
.legal .links{left:27px;top:20px;font-size:5.4px}
.legal .copy{left:27px;top:33px;font-size:5.4px}
.cards{left:512px;top:24px;display:flex;gap:7px}
.cards span{width:21px;height:14px;background:var(--white);border-radius:2px}
</style>
</head>
<body>

<header>
  <div class="abs social-dots"><span></span><span></span><span></span><span></span><span></span></div>
  <div class="abs account-links"><span class="login">LOGIN/REGISTER</span> &nbsp;| &nbsp;MY ACCOUNT &nbsp;| &nbsp;WISHLIST - 0</div>
  <form class="abs search"><input value="Enter keyword" aria-label="Search"><button type="button">SEARCH</button></form>
  <div class="abs brand-name header-brand">Hire a Lantern</div>
  <div class="abs cart">
    <svg width="9" height="8" viewBox="0 0 9 8"><path d="M0 1h2l1 4h5l1-3H3" fill="none" stroke="#e31b23" stroke-width="1"/><circle cx="3.5" cy="7" r=".8" fill="#e31b23"/><circle cx="7" cy="7" r=".8" fill="#e31b23"/></svg>
    <span>CART :</span><span>&nbsp;&nbsp;0 (items)</span><span class="caret"></span>
  </div>
</header>

<nav class="abs nav">
  <svg class="abs" style="left:40px;top:9px" width="12" height="11" viewBox="0 0 12 11"><path d="M6 0L0 5.5h1.6V11h3.2V7.5h2.4V11h3.2V5.5H12z" fill="#fff"/></svg>
  <span class="sep" style="left:66px"></span>
  <a style="left:82px">ABOUT</a><span class="sep" style="left:99px"></span>
  <a style="left:139px">NEW PRODUCT</a><span class="sep" style="left:171px"></span>
  <a style="left:206px">SPECIAL CANDLE</a><span class="sep" style="left:244px"></span>
  <a style="left:264px">FAQS</a><span class="sep" style="left:283px"></span>
  <a style="left:314px">ACCESSORIES</a><span class="sep" style="left:346px"></span>
  <a style="left:370px">REVIEWS</a><span class="sep" style="left:393px"></span>
  <a style="left:432px">PILLAR CANDLES</a><span class="sep" style="left:471px"></span>
  <a style="left:495px">CONTACT US</a>
  <a class="checkout">CHECKOUT &#10140;</a>
</nav>

<section class="abs hero">
  <div class="abs hero-photo" role="img" aria-label="Rows of lit tea-light candles glowing on a dark reflective table"></div>
  <div class="abs hero-copy">LATEST MODEL DESIGN<br>CANDLE RENDAL FOR<br><span class="hot">25%</span> OFF</div>
  <div class="abs btn-solid shop">SHOP NOW</div>
  <div class="abs dots"><span></span><span></span><span></span><span></span></div>
</section>

<section>
  <div class="abs tile wedding" role="img" aria-label="Wedding table decorated with lanterns, flowers and small candles">
    <div class="abs tile-title overlay-band" style="top:59px">Wedding Candle</div>
  </div>
  <div class="abs tile pillar" role="img" aria-label="Lit red pillar candles with soft bokeh lights">
    <div class="abs tile-title">Pillar Candles</div>
    <div class="abs btn-outline">SHOP NOW</div>
  </div>
  <div class="abs tile framed special">
    <div class="abs inner">
      <div class="abs tile-title">Special &nbsp;Candle</div>
      <div class="abs btn-outline">SHOP NOW</div>
    </div>
  </div>
  <div class="abs tile framed latest">
    <div class="abs inner">
      <div class="abs tile-title">Latest Model<br>Candle</div>
      <div class="abs btn-outline">SHOP NOW</div>
    </div>
  </div>
  <div class="abs tile newmodel" role="img" aria-label="White rose centrepiece with glass candle holders">
    <div class="abs tile-title overlay-band" style="top:59px">New Model Candle</div>
  </div>
</section>

<section class="abs newsletter">
  <h2 class="abs section-title">Newsletter Sign Up</h2>
  <p class="abs">Lorem ipsum dolor sit amet conse ctetur adipisicing elit, sed do eiusmod tempor incididunt ut labore.Lorem ipsum dolor sit amet co.nse ctetur adipisicing elit, sed do eiusmod tempor incididunt ut labore Lorem ipsum dolor sit amet conse ctetur adipisicing elit, sed do eiusmod tempor incididunt ut &nbsp;incididunt ut labore Lorem ipsum dolor sit amet labore</p>
  <form class="abs subscribe"><input value="Enter Your E-Mail Id" aria-label="Email"><button type="button">SUBSCRIBE</button></form>
  <div class="abs divider-v"></div>
  <div class="follow">
    <h2 class="abs section-title">Follow Us</h2>
    <a class="a">Flamebook</a>
    <a class="b">Chirper</a>
    <a class="c">LinkRoll</a>
  </div>
</section>

<footer class="abs footer">
  <div class="abs brand-name footer-brand">Hire a Lantern</div>
  <div class="abs divider-v" style="left:206px"></div>
  <div class="abs col" style="left:223px"><h3>Important Links</h3><ul><li>Affiliate Program</li><li>Special Promotions</li><li>Newsletter</li><li>Contact</li></ul></div>
  <div class="abs divider-v" style="left:361px"></div>
  <div class="abs col" style="left:380px"><h3>Customer Service</h3><ul><li>Contact Us</li><li>Returns</li><li>Site Map</li><li>Forget Password</li></ul></div>
  <div class="abs divider-v" style="left:518px"></div>
  <div class="abs col" style="left:538px"><h3>My Account</h3><ul><li>AMy Account</li><li>Order History</li><li>Wish List</li><li>Newsletter</li></ul></div>
</footer>

<div class="abs legal">
  <div class="abs links">Policies &nbsp;| &nbsp;Privacy &nbsp;| &nbsp;Terms &amp; Conditions</div>
  <div class="abs copy">Copyright 2016 Company Name. &nbsp;All Rights Reserved.</div>
  <div class="abs cards"><span></span><span></span><span></span><span></span><span></span></div>
</div>

</body>
</html>
```